Need a business cards for a hair dressing salon.

Target Market(s)

Target woman for Hair cuts, bridal makeup, occasion, fashion makeup and etc.

Industry/Entity Type

Hair

Font styles to use
Serif
Script

Requirements
Must have
• - Business card to be memorable and recognizable

- Please include the following on the business card:
- Business name: Salon Marolin
- Name: Nilumi Jayasekara (Name Must be changeable)
- Occupation: Hair Dresser & Beautician
- Contact number: 04 731 6 CURL
- Email: mail@marolin.com.au
- Facebook (please use image): www.facebook.com/marolin.com.au
Nice to have
• Font Styles:
Business Name - Script
Other Text - Serif

```html
<!DOCTYPE html>
<html lang="en">
<head>
<meta charset="utf-8">
<title>Salon Marolin – Business Card</title>
<link rel="stylesheet" href="https://fonts.googleapis.com/css2?family=Questrial&display=swap">
<style>
  :root {
    --backdrop: #2a2a2a;
    --card-dark: #1e1e1e;
    --card-dark-edge: #2c2c2c;
    --card-light: #ffffff;
    --card-light-shade: #ececec;
    --ink: #3a3a3a;
    --ink-soft: #6a6a6a;
    --ink-on-dark: #d8d8d8;
    --rule: #c4c4c4;
    --mark-tint: #e6e6e6;
  }
  * { margin: 0; padding: 0; box-sizing: border-box; }
  html, body {
    width: 1200px; height: 900px; overflow: hidden;
    background: var(--backdrop);
    font-family: "Questrial", "Helvetica Neue", Arial, sans-serif;
  }
  .canvas { position: relative; width: 1200px; height: 900px; }

  .card {
    position: absolute;
    width: 560px; height: 320px;
    border-radius: 3px;
    box-shadow: 0 14px 30px rgba(0,0,0,0.45);
    overflow: hidden;
  }

  /* back side */
  .card--back {
    left: 90px; top: 100px;
    background: linear-gradient(160deg, var(--card-dark-edge), var(--card-dark));
    display: flex; align-items: center; justify-content: center;
  }
  .card--back .wordmark { color: var(--ink-on-dark); font-size: 40px; }

  /* front side */
  .card--front {
    left: 550px; top: 470px;
    background: linear-gradient(180deg, var(--card-light) 55%, var(--card-light-shade));
  }
  .wordmark {
    font-family: "Questrial", "Helvetica Neue", Arial, sans-serif;
    font-weight: 400;
    letter-spacing: 1px;
    white-space: nowrap;
  }
  .card--front .wordmark {
    position: absolute; right: 60px; top: 52px;
    color: var(--ink); font-size: 38px;
  }
  .monogram-area {
    position: absolute; right: -30px; top: 110px;
    width: 230px; height: 230px; border-radius: 50%;
    background: radial-gradient(circle, var(--mark-tint), rgba(230,230,230,0) 70%);
  }
  .holder {
    position: absolute; left: 40px; top: 150px;
  }
  .holder__name {
    color: var(--ink); font-size: 18px; letter-spacing: 1.5px;
    text-transform: uppercase; font-weight: 400;
  }
  .holder__role { color: var(--ink-soft); font-size: 14px; margin-top: 2px; }

  .contact {
    position: absolute; left: 40px; bottom: 34px;
    display: flex; gap: 12px; align-items: stretch;
  }
  .contact__icons {
    display: flex; flex-direction: column; justify-content: space-between;
    padding: 2px 0;
  }
  .contact__icons svg { width: 13px; height: 13px; display: block; }
  .contact__rule { width: 1px; background: var(--rule); }
  .contact__lines { list-style: none; color: var(--ink); font-size: 14px; line-height: 19px; }
</style>
</head>
<body>
<main class="canvas">
  <section class="card card--back" aria-label="Card back">
    <span class="wordmark">Salon Marolin</span>
  </section>

  <section class="card card--front" aria-label="Card front">
    <div class="monogram-area" role="img" aria-label="Faint monogram decoration"></div>
    <span class="wordmark">Salon Marolin</span>

    <div class="holder">
      <h1 class="holder__name">Nilumi Jayasekara</h1>
      <p class="holder__role">Hair Dresser &amp; Beautician</p>
    </div>

    <div class="contact">
      <div class="contact__icons">
        <svg viewBox="0 0 16 16" aria-hidden="true"><path fill="#3a3a3a" d="M3 1.5l2.5-.5 1.5 3.5-1.8 1.2a8 8 0 0 0 4.6 4.6l1.2-1.8 3.5 1.5-.5 2.5c-.3.8-1 1-2 1C6.5 13.5 2.5 9.5 2 4c0-1 .2-1.9 1-2.5z"/></svg>
        <svg viewBox="0 0 16 16" aria-hidden="true"><rect x="1" y="3.5" width="14" height="9" fill="none" stroke="#3a3a3a" stroke-width="1.4"/><path d="M1 3.5l7 5 7-5" fill="none" stroke="#3a3a3a" stroke-width="1.4"/></svg>
        <svg viewBox="0 0 16 16" aria-hidden="true"><circle cx="8" cy="8" r="6" fill="#3a3a3a"/></svg>
      </div>
      <span class="contact__rule"></span>
      <ul class="contact__lines">
        <li>04 731 6 CURL</li>
        <li>mail@marolin.com.au</li>
        <li>/marolin.com.au</li>
      </ul>
    </div>
  </section>
</main>
</body>
</html>
```